Hotel Lobby sign up to invest banner 4ft by 8 ft

We need to have a 4ft x 8ft banner designed. the sign is to attract investors to purchase condos at The Lodge at Marlowe's Bend. Banner will hang in lobby and an ipad will be available for guest to sign up to get information and investor information.
The wording used should be something similar to or:

You Love the Resort, why not own it?

Sign-Up Here to receive updates & new condo information

Target Market(s)

Condo guest looking to invest

Industry/Entity Type

Hospitality

Requirements
Must have
• Logo and be 4ft by 8 ft
Nice to have
• use the attached map but does not have to
• font has to be eligible
Should not have
• scripted font

```html
<!DOCTYPE html>
<html lang="en">
<head>
<meta charset="utf-8">
<title>The Lodge at Marlowe's Bend – Condo Sign Up Banner</title>
<link rel="stylesheet" href="https://fonts.googleapis.com/css2?family=Open+Sans:ital,wght@0,300;0,400;0,700;0,800;1,400&display=swap">
<style>
  :root {
    --tan: #D49E62;
    --tan-faint: #DCAC75;
    --white: #FFFFFF;
    --cream: #F7EBDB;
    --ink: #3A3835;
    --teal: #5A7F8A;
    --teal-shadow: #6A4E30;
    --brown: #5B4434;
    --logo-ink: #3E2C1E;
    --map-green: #8FAA76;
    --map-grey: #C3C4BC;
    --map-light: #DADCD3;
  }
  * { margin: 0; padding: 0; box-sizing: border-box; }
  html, body { width: 1200px; height: 2396px; overflow: hidden; background: var(--tan); }
  .banner {
    position: relative;
    width: 1200px;
    height: 2396px;
    overflow: hidden;
    font-family: "Open Sans", Arial, sans-serif;
  }
  .banner__shapes { position: absolute; inset: 0; }
  .brand {
    position: absolute;
    top: 170px; left: 0; width: 1200px;
    text-align: center;
    color: var(--logo-ink);
    font-weight: 800;
    line-height: 1.05;
  }
  .brand__name { display: block; font-size: 130px; }
  .brand__place { display: block; font-size: 56px; margin-top: 18px; }
  .watermark {
    position: absolute;
    top: 1200px; left: 0; width: 1200px;
    text-align: center;
    color: var(--tan-faint);
    font-weight: 700;
    line-height: 1;
  }
  .watermark__name { display: block; font-size: 250px; }
  .watermark__place { display: block; font-size: 100px; margin-top: 30px; }
  .headline {
    position: absolute;
    top: 1060px; left: 0; width: 1200px;
    text-align: center;
  }
  .headline__lead {
    display: block;
    font-size: 74px; font-weight: 300;
    color: var(--cream);
    letter-spacing: -1px;
  }
  .headline__question {
    display: block;
    font-size: 104px; font-weight: 700;
    color: var(--ink);
    letter-spacing: -2px;
    margin-top: -6px;
  }
  .cta {
    position: absolute;
    top: 1450px; left: 254px;
    width: 686px; height: 440px;
    background: var(--teal);
    box-shadow: 30px 30px 0 var(--teal-shadow);
    display: flex; flex-direction: column;
    align-items: center; justify-content: center;
    color: var(--white);
    font-weight: 700;
    line-height: 0.95;
    text-shadow: 7px 7px 0 var(--tan);
  }
  .cta__top { font-size: 150px; letter-spacing: -3px; }
  .cta__bottom { font-size: 214px; letter-spacing: -4px; }
  .footnote {
    position: absolute;
    top: 2225px; left: 0; width: 1200px;
    text-align: center;
    color: var(--white);
    font-style: italic;
    font-weight: 400;
    font-size: 68px;
    line-height: 1.18;
    letter-spacing: -1px;
  }
</style>
</head>
<body>
<main class="banner">
  <svg class="banner__shapes" width="1200" height="2396" viewBox="0 0 1200 2396" aria-hidden="false">
    <defs>
      <linearGradient id="mapTone" x1="0" y1="0" x2="1" y2="1">
        <stop offset="0" stop-color="var(--map-grey)"/>
        <stop offset="0.45" stop-color="var(--map-light)"/>
        <stop offset="1" stop-color="var(--map-green)"/>
      </linearGradient>
    </defs>
    <rect class="site-map" x="0" y="0" width="1200" height="920" fill="url(#mapTone)" role="img" aria-label="Aerial map of the resort grounds with buildings, roads, lawns and the outdoor pool"/>
    <polygon class="chevron-top__edge" points="0,585 600,870 1200,585 1200,2396 0,2396" fill="var(--white)"/>
    <polygon class="chevron-top__field" points="0,620 600,905 1200,620 1200,2396 0,2396" fill="var(--tan)"/>
    <polygon class="chevron-bottom__edge" points="0,2150 600,2070 1200,2150 1200,2396 0,2396" fill="var(--white)"/>
    <polygon class="chevron-bottom__field" points="0,2185 600,2105 1200,2185 1200,2396 0,2396" fill="var(--brown)"/>
  </svg>

  <div class="brand">
    <span class="brand__name">The Lodge</span>
    <span class="brand__place">at Marlowe's Bend</span>
  </div>

  <div class="watermark" aria-hidden="true">
    <span class="watermark__name">The Lodge</span>
    <span class="watermark__place">at Marlowe's Bend</span>
  </div>

  <h1 class="headline">
    <span class="headline__lead">You Love The Lodge,</span>
    <span class="headline__question">Why Not Own It ?</span>
  </h1>

  <div class="cta">
    <span class="cta__top">SIGN UP</span>
    <span class="cta__bottom">HERE</span>
  </div>

  <p class="footnote">to Receive Updates<br>&amp; New Condo Information</p>
</main>
</body>
</html>
```